*YO!!! Designers Needed...Again!!* 1 Page Cover Needed for a $$Billion Dollar$$ Company (Contest)

After 2 successful projects on PixelGuild, we're back again and need YOUR help! Last time we needed a front page cover for our annual report. This time we're seeking one for our annual catalog.

We are a manufacturer of aluminum electrolytic capacitors. We are a publicly listed company and work with many Meridian 400 companies, so your work will be viewed by the BIG GUNS and EXECUTIVES around the WORLD! If selected, you may be selected for additional work. The catalog will be distributed to all of our clients as well as be distributed at major trade shows in 2021 and 2022.

The cover should be unique. If colorful, modern, artistic, and creativity somehow got together and had a child, that's what the cover page would look like!

Inspired Examples attached. Check them out!

www.korvane.example

Target Market(s)

Consumers, Purchasers, Engineers

Industry/Entity Type

Electronic

Font styles to use
Sans Serif

Requirements
Must have
• 1. Must include the attached Korvane logo. Logo size, color, and placement are at your discretion.

2. Include the text, 'Aluminum Electrolytic Capacitors' (upper case or lower case is up to you) '2021/22'

3. Shall be in A4 size and vertical orientation.
Nice to have
• Feel free to add any icons or stock photos (for example capacitors or circuit boards) if needed. For ones requiring payments, add the stock graphic example and if we like it, provide the link/source and we will pay for it.

Feel free to use any of the capacitor icon attachments if you think it will help. These are optional and not required. Can photoshop as needed.

Be creative here and don't be afraid to be bold! The end product will be printed into a physical catalog.

Our slogan is "Think Ahead". This slogan can or cannot be part of the theme.

```html
<!DOCTYPE html>
<html lang="en">
<head>
<meta charset="utf-8">
<title>Korvane Annual Report 2021-22</title>
<link href="https://fonts.googleapis.com/css2?family=Roboto:wght@300;400;500;700;900&display=swap" rel="stylesheet">
<style>
  :root {
    --navy: #062f63;
    --teal: #00a99d;
    --blue: #1f76c1;
    --green-light: #7bbf7f;
    --green-mid: #2fae97;
    --mint: #a4d1c5;
    --paper: #ffffff;
  }
  html, body {
    margin: 0;
    padding: 0;
    width: 848px;
    height: 1200px;
    overflow: hidden;
    background: var(--paper);
  }
  .cover {
    position: relative;
    width: 848px;
    height: 1200px;
    overflow: hidden;
    background: var(--paper);
    font-family: "Roboto", sans-serif;
  }
  .brand-name {
    position: absolute;
    left: 37px;
    top: 48px;
    margin: 0;
    font-size: 46px;
    font-weight: 700;
    color: var(--navy);
    line-height: 1;
    letter-spacing: 0.5px;
  }
  .corner-triangle {
    position: absolute;
    left: 0;
    top: 0;
  }
  .year {
    position: absolute;
    right: 34px;
    top: 199px;
    margin: 0;
    font-size: 29px;
    font-weight: 500;
    color: var(--navy);
    letter-spacing: 2px;
    line-height: 1.2;
  }
  .title {
    position: absolute;
    right: 32px;
    top: 231px;
    margin: 0;
    font-size: 60px;
    font-weight: 900;
    color: var(--teal);
    letter-spacing: 4px;
    line-height: 1.2;
    white-space: nowrap;
  }
  .title-rule {
    position: absolute;
    left: 400px;
    right: 34px;
    top: 303px;
    height: 4px;
    background: linear-gradient(90deg, rgba(6,47,99,0) 0%, #9fb9d4 25%, #1f5a96 80%, var(--navy) 100%);
  }
  .subtitle {
    position: absolute;
    right: 34px;
    top: 315px;
    margin: 0;
    font-size: 35px;
    color: var(--blue);
    letter-spacing: 1px;
    line-height: 1.2;
    white-space: nowrap;
  }
  .subtitle .light { font-weight: 300; }
  .subtitle .medium { font-weight: 500; }
  .subtitle .bold { font-weight: 900; }
  .pattern-field {
    position: absolute;
    left: 0;
    top: 0;
  }
</style>
</head>
<body>
  <main class="cover">
    <svg class="pattern-field" width="848" height="1200" viewBox="0 0 848 1200" role="img" aria-label="Perspective field of blue triangles receding into the distance, fading from light grey-blue to deep navy">
      <defs>
        <linearGradient id="fieldTone" x1="0" y1="0" x2="0" y2="1">
          <stop offset="0" stop-color="#dfe5ee" stop-opacity="0"/>
          <stop offset="0.15" stop-color="#c9d3e1"/>
          <stop offset="0.5" stop-color="#6d8bb0"/>
          <stop offset="1" stop-color="var(--navy)"/>
        </linearGradient>
      </defs>
      <path d="M300 300 C340 290 380 320 400 360 C470 440 620 560 848 830 L848 1200 L0 1200 L0 720 C60 620 140 520 200 440 C240 380 270 330 300 300 Z" fill="url(#fieldTone)"/>
    </svg>

    <svg class="corner-triangle" width="848" height="200" viewBox="0 0 848 200" aria-hidden="true">
      <defs>
        <linearGradient id="cornerTone" x1="650" y1="170" x2="800" y2="30" gradientUnits="userSpaceOnUse">
          <stop offset="0" stop-color="var(--mint)"/>
          <stop offset="0.5" stop-color="var(--green-mid)"/>
          <stop offset="0.75" stop-color="var(--green-light)"/>
          <stop offset="1" stop-color="var(--green-light)"/>
        </linearGradient>
      </defs>
      <polygon points="809,4 647,96 809,190" fill="url(#cornerTone)"/>
    </svg>

    <p class="brand-name">Korvane</p>

    <p class="year">2021-22</p>
    <h1 class="title">ANNUAL REPORT</h1>
    <div class="title-rule"></div>
    <h2 class="subtitle"><span class="light">ALUMINUM</span> <span class="medium">ELECTROLYTIC</span> <span class="bold">CAPACITORS</span></h2>
  </main>
</body>
</html>
```